Premium Classic Tea Box Packaging Design

We are going to launch a new product of premium classic tea using Tongkat Ali ingredient. We are looking for the tea box packaging design for our product that named Rui Feng 瑞丰. Both english and chinese name should be included in the packaging design. Product origin from Malaysia.

Other things that should be included in the design are
- website url "www.ruifeng.my"
- Premium Tea
- Slogan "Live Live to the Fullest
- 100% All Natural Ingredients
- 养生保健,首选咖啡

The product content is 20 tea bags. The size of the package is rectangular, Size: Box - 180 x 125 x 40 mm (Pizza Box Style of opening). Consumers would open the packaging box and see the tea bags lies inside similar to this . http://tnk.gx/Rm4Pw8

We are looking for design that gives us the feeling of
- classy feeling
- strong
- confidence
- a combination of chinese and western design style (optional)
- gentleman
- expensive / high end

This is a premium product and design should symbolise health, hope, wellness and prosperity

We would like to see designs that use the shining color
- shining black
- gold
- green
However if you deem that other colors can be more suitable, we are open to new ideas.

I am looking for creative ideas that are able to capture people attention with its elegance.

Example of designs that we like :
http://tnk.gx/Hq7Ls2
http://tnk.gx/Yd3Kf9
http://tnk.gx/Wp5Ns1
http://tnk.gx/Gm8Xv4
http://tnk.gx/Qc2Rt7 / http://tnk.gx/Jn6Hw3
http://tnk.gx/Fs9Dk5
http://tnk.gx/Vb4Ym8
http://tnk.gx/Kx1Pe6

Close/Similar company to reference : KMP / Premium Harrowdale

Reason: Hi all, thank you for your submission. We will be replying to proposal and discuss improvements that could be make, if possible, please try to change design to using dark -ish shining green as background. For those who intending to submit your proposal, please do so. Thank you for all the proposal.

Target Market(s)

Our target market men from the China market.

Industry/Entity Type

Health And Wellness

Font styles to use
Decorative
Script

Requirements
Must have
• Both english and chinese name should be included in the packaging design. Product origin from Malaysia.
• Other things that should be included in the design are
• - website url "www.ruifeng.my"
• - Premium Tea
• - Slogan "Live Live to the Fullest
• - 100% All Natural Ingredients
• - 养生保健,首选咖啡

```html
<!DOCTYPE html>
<html lang="en">
<head>
<meta charset="utf-8">
<title>Rui Feng Premium Tea – Box Front</title>
<link href="https://fonts.googleapis.com/css2?family=Great+Vibes&family=Libre+Baskerville:wght@700&family=Noto+Serif+SC:wght@400;700&family=Noto+Serif:wght@400;700&display=swap" rel="stylesheet">
<style>
  :root {
    --page-bg: #ffffff;
    --box-dark: #2b2728;
    --box-dark-light: #3a3536;
    --box-dark-deep: #1f1c1d;
    --gold: #b9aa1e;
    --slogan-grey: #a3aa9c;
    --cn-white: #f4f4f0;
    --url-tone: #a49c82;
    --lid-yellow: #f2e400;
    --lid-yellow-shade: #c9b800;
    --leaf-green: #3f9a2c;
    --leaf-light: #7fcf4a;
    --badge-green: #4fae24;
    --badge-light: #9be04f;
    --badge-rim: #e8f5d6;
    --badge-text: #ffffff;
  }
  html, body {
    margin: 0;
    padding: 0;
    width: 1200px;
    height: 1182px;
    overflow: hidden;
    background: var(--page-bg);
  }
  .canvas {
    position: relative;
    width: 1200px;
    height: 1182px;
  }
  .box-front {
    position: absolute;
    left: 252px;
    top: 100px;
    width: 708px;
    height: 925px;
    background:
      radial-gradient(ellipse at 70% 75%, var(--box-dark-light) 0%, transparent 60%),
      linear-gradient(180deg, var(--box-dark-deep) 0%, var(--box-dark) 40%, var(--box-dark-light) 100%);
    box-shadow: 0 4px 14px rgba(0,0,0,0.35);
  }
  .lid-band {
    position: absolute;
    left: 252px;
    top: 978px;
    width: 706px;
    height: 123px;
  }
  .brand-name {
    position: absolute;
    left: 252px;
    width: 708px;
    top: 150px;
    margin: 0;
    text-align: center;
    font-family: "Noto Serif", "Noto Serif SC", serif;
    font-weight: 700;
    font-size: 30px;
    letter-spacing: 3px;
    color: var(--gold);
  }
  .title {
    position: absolute;
    left: 252px;
    width: 708px;
    top: 212px;
    margin: 0;
    text-align: center;
    font-family: "Great Vibes", cursive;
    font-weight: 400;
    font-size: 108px;
    line-height: 1;
    color: var(--gold);
  }
  .slogan {
    position: absolute;
    left: 252px;
    width: 708px;
    top: 345px;
    margin: 0;
    text-align: center;
    font-family: "Libre Baskerville", serif;
    font-weight: 700;
    font-size: 37px;
    color: var(--slogan-grey);
  }
  .slogan-cn {
    position: absolute;
    left: 252px;
    width: 708px;
    top: 415px;
    margin: 0;
    text-align: center;
    font-family: "Noto Serif SC", serif;
    font-size: 40px;
    letter-spacing: 2px;
    color: var(--cn-white);
  }
  .herb-illustration {
    position: absolute;
    left: 420px;
    top: 485px;
    width: 430px;
    height: 345px;
    border-radius: 45% 40% 50% 45%;
    background: radial-gradient(ellipse at 45% 45%, var(--leaf-light) 0%, var(--leaf-green) 55%, rgba(63,154,44,0) 75%);
  }
  .natural-leaves {
    position: absolute;
    left: 266px;
    top: 826px;
    width: 104px;
    height: 160px;
    border-radius: 50%;
    background: radial-gradient(ellipse at 55% 45%, var(--badge-light) 0%, var(--leaf-green) 60%, rgba(63,154,44,0) 75%);
  }
  .natural-badge {
    position: absolute;
    left: 358px;
    top: 827px;
    width: 134px;
    height: 134px;
    border-radius: 50%;
    background: radial-gradient(circle at 40% 35%, var(--badge-light) 0%, var(--badge-green) 70%);
    box-shadow: 0 0 0 5px var(--badge-rim);
    display: flex;
    flex-direction: column;
    align-items: center;
    justify-content: center;
    text-align: center;
    font-family: "Noto Serif", serif;
    font-weight: 700;
    color: var(--badge-text);
    line-height: 1.1;
  }
  .natural-badge .badge-percent { font-size: 28px; }
  .natural-badge .badge-line { font-size: 13px; letter-spacing: 1px; }
  .site-url {
    position: absolute;
    left: 700px;
    width: 240px;
    top: 958px;
    margin: 0;
    text-align: center;
    font-family: "Noto Serif", serif;
    font-size: 24px;
    color: var(--url-tone);
  }
  .origin {
    position: absolute;
    left: 700px;
    width: 240px;
    top: 992px;
    margin: 0;
    text-align: center;
    font-family: "Noto Serif", serif;
    font-size: 15px;
    letter-spacing: 1px;
    color: var(--url-tone);
  }
</style>
</head>
<body>
<main class="canvas">
  <div class="box-front"></div>

  <svg class="lid-band" viewBox="0 0 706 123" aria-hidden="true">
    <defs>
      <linearGradient id="lidFill" x1="0" y1="0" x2="0" y2="1">
        <stop offset="0" stop-color="var(--lid-yellow)"/>
        <stop offset="1" stop-color="var(--lid-yellow-shade)"/>
      </linearGradient>
    </defs>
    <path d="M0 41 H303 C318 41 318 0 340 0 H398 C420 0 420 41 435 41 H706 V123 H0 Z" fill="url(#lidFill)"/>
  </svg>

  <p class="brand-name">Rui Feng 瑞丰</p>
  <h1 class="title">Premium Tea</h1>
  <p class="slogan">Live Live to the Fullest</p>
  <p class="slogan-cn">养生保健，首选咖啡</p>

  <div class="herb-illustration" role="img" aria-label="Illustration of a Tongkat Ali herb sprig with green leaves"></div>

  <div class="natural-leaves" role="img" aria-label="Illustration of fresh green leaves"></div>
  <div class="natural-badge">
    <span class="badge-percent">100%</span>
    <span class="badge-line">ALL NATURAL</span>
    <span class="badge-line">INGREDIENTS</span>
  </div>

  <p class="site-url">www.ruifeng.my</p>
  <p class="origin">Product of Malaysia</p>
</main>
</body>
</html>
```